Business cards for start-up accounting firm

I'm looking for a double sided business card ready for upload into Lumo print or similar print providers with no modification required by me.
I'm looking for something simple as i think cards that are too 'busy' actually detract from the message. I have some thoughts but more than happy to see what comes up. The logo i have came out of left field and i love it the moment i saw it!

My thoughts:

Side 1: Just the logo, perhaps on a dark grey or charcoal background to make the logo colours stand out?

Side 2: The call to action from me website 'Looking for a more relaxed, friendly and interactive relationship with your accountant?' with my contact information
Name: Gus Tarrow
Email: gus@ledgerowl.com.au
Website: www.ledgerowl.com.au
Phone: 1300 762 349

The call to action needs to be the first thing they see when they look at side 2. If it helps to know what we do and how we do it there is a draft website at www.ledgerowl.com.au

Like i said, happy to consider anything that comes up :)

Target Market(s)

i'm targeting small business owners who experience a lot of stress around finacial reporting and have had bad experiences with accountants in the past.

Industry/Entity Type

Accounting

Contact Information for Business Card

Contained in the Description

Font styles to use
Serif
Sans Serif
Other font styles liked:
• See logo files attached

Colors
474747

Requirements
Must have
• My logo, slogan and contact information

```html
<!DOCTYPE html>
<html lang="en">
<head>
<meta charset="utf-8">
<title>Ledger Owl business cards</title>
<link rel="stylesheet" href="https://fonts.googleapis.com/css2?family=Open+Sans:wght@400;600;700&display=swap">
<style>
  :root {
    --backdrop: #6a4a37;
    --card-light: #ffffff;
    --card-dark: #2b2b2b;
    --plum: #7b2d6e;
    --brand-text: #f2f2f2;
    --slogan-text: #b5b5b5;
    --ink: #1f1f1f;
  }
  * { box-sizing: border-box; margin: 0; padding: 0; }
  html, body { width: 1200px; height: 1000px; overflow: hidden; }
  body {
    background: var(--backdrop);
    font-family: "Open Sans", Arial, sans-serif;
    position: relative;
  }
  .card {
    position: absolute;
    left: 265px;
    width: 665px;
    height: 397px;
    border-radius: 24px;
    overflow: hidden;
  }
  .card--contact { top: 73px; background: var(--card-light); }
  .card--brand { top: 532px; background: var(--card-dark); }

  .call-to-action {
    position: absolute;
    top: 128px; left: 0; right: 0;
    text-align: center;
    color: var(--plum);
    font-weight: 600;
    font-size: 21px;
    line-height: 29px;
  }
  .holder-name {
    position: absolute;
    top: 273px; left: 0; right: 0;
    text-align: center;
    color: var(--ink);
    font-size: 17px;
    letter-spacing: 0.3px;
    text-transform: uppercase;
  }
  .divider {
    position: absolute;
    top: 316px; left: 40px; right: 40px;
    height: 2px;
    background: linear-gradient(90deg, rgba(0,0,0,0) 0%, #222 50%, rgba(0,0,0,0) 100%);
  }
  .contact-row {
    position: absolute;
    top: 336px; left: 38px; right: 38px;
    display: flex;
    justify-content: space-between;
    align-items: center;
    font-size: 15px;
    color: var(--ink);
  }
  .contact-item { display: flex; align-items: center; gap: 7px; white-space: nowrap; }
  .contact-item svg { width: 15px; height: 15px; fill: var(--plum); }

  .brand-name {
    position: absolute;
    top: 128px; left: 0; right: 0;
    text-align: center;
    color: var(--brand-text);
    font-weight: 700;
    font-size: 70px;
    line-height: 96px;
    letter-spacing: 1px;
    text-transform: uppercase;
  }
  .slogan {
    position: absolute;
    top: 256px; left: 0; right: 0;
    text-align: center;
    color: var(--slogan-text);
    font-size: 16px;
    letter-spacing: 1.6px;
    text-transform: uppercase;
    white-space: nowrap;
  }
</style>
</head>
<body>
  <section class="card card--contact">
    <p class="call-to-action">Looking for a more relaxed, friendly and interactive<br>relationship with your accountant?</p>
    <p class="holder-name">Gus Tarrow</p>
    <div class="divider"></div>
    <div class="contact-row">
      <span class="contact-item">
        <svg viewBox="0 0 16 16" aria-hidden="true"><path d="M2 5c0-2 2-3 6-3s6 1 6 3v1h-3V5H5v1H2z"/><path d="M4 7h8l2 6H2z M8 8.5a2 2 0 1 0 0 4 2 2 0 0 0 0-4z"/></svg>
        1300 762 349
      </span>
      <span class="contact-item">
        <svg viewBox="0 0 16 16" aria-hidden="true"><path d="M1 4h14v9H1z M2 4.5l6 4.5 6-4.5" stroke="#fff" stroke-width="1"/></svg>
        gus@ledgerowl.com.au
      </span>
      <span class="contact-item">
        <svg viewBox="0 0 16 16" aria-hidden="true"><circle cx="8" cy="8" r="6.5" fill="none" stroke="var(--plum)" stroke-width="1.6"/><path d="M1.5 8h13M8 1.5c-3 3-3 10 0 13M8 1.5c3 3 3 10 0 13" fill="none" stroke="var(--plum)" stroke-width="1.2"/></svg>
        www.ledgerowl.com.au
      </span>
    </div>
  </section>

  <section class="card card--brand">
    <p class="brand-name">Ledger Owl</p>
    <p class="slogan">Calm books, clear growth</p>
  </section>
</body>
</html>
```